Create a label for a new apple cider beverage

For the first time this year, we create our own apple cider.

We need an idea for the label for the bottle.

The cider is produced in a small village in Switzerland. Years ago many people were produing cider in this village but because of structural changes, the know-how and the apple cider itself got lost in our village. The last man creating apple cider in our village was called Jakob-Ruedi. In respect to this man, we would like to call our apple cider Jakob-Ruedi.

The proposed label should include the following ideas / spezification:
- a picture of a stylized old farmer
- a picture of an apple
- emblem of the village as added to this request ([login to view URL])
- only use 4 colors
- size of the label 99 x 85 mm

```html
<!DOCTYPE html>
<html lang="en">
<head>
<meta charset="utf-8">
<title>Jakob-Ruedi Apple Cider Label</title>
<link href="https://fonts.googleapis.com/css2?family=Gochi+Hand&family=Kaushan+Script&family=Arimo:wght@400;700&display=swap" rel="stylesheet">
<style>
  :root {
    --wine: #6e0b0e;
    --red: #b5141b;
    --bright-red: #d8262b;
    --cream: #ffffff;
    --gold-deep: #d99a12;
    --apple: #9ccc5a;
    --apple-dark: #4f8a2c;
    --ink: #222;
    --page: #eeeeee;
  }
  * { margin: 0; padding: 0; box-sizing: border-box; }
  html, body { width: 800px; height: 1200px; overflow: hidden; background: var(--page); }
  .canvas { position: relative; width: 800px; height: 1200px; }
  .label {
    position: absolute; left: 80px; top: 200px; width: 640px; height: 800px;
    background: linear-gradient(180deg, var(--wine) 0%, var(--red) 30%, var(--bright-red) 52%, #e98a8a 66%, var(--cream) 80%, var(--cream) 100%);
    overflow: hidden;
    box-shadow: 0 6px 18px rgba(0,0,0,.18);
  }
  .category {
    position: absolute; left: 0; right: 0; top: 40px; text-align: center;
    font-family: "Arimo", sans-serif; font-weight: 700; font-size: 34px;
    color: var(--cream); letter-spacing: 2px;
  }
  .product-name {
    position: absolute; left: 0; right: 0; top: 108px; text-align: center;
    font-family: "Gochi Hand", cursive; font-size: 96px; color: var(--cream);
    letter-spacing: 1px; text-shadow: 3px 4px 0 rgba(60,0,0,.55);
  }
  .glow {
    position: absolute; left: 170px; top: 220px; width: 300px; height: 180px;
    background: radial-gradient(ellipse at center, #f0a020 0%, rgba(240,120,20,.4) 50%, rgba(240,120,20,0) 75%);
  }
  .apple-photo {
    position: absolute; left: 205px; top: 240px; width: 240px; height: 170px;
    border-radius: 48% 52% 46% 54%;
    background: radial-gradient(circle at 40% 40%, #e7f3c8 0%, var(--apple) 45%, var(--apple-dark) 100%);
  }
  .product-type {
    position: absolute; left: 50%; top: 458px; transform: translateX(-50%);
    padding: 8px 30px; background: var(--wine); border: 2px solid var(--cream);
    font-family: "Arimo", sans-serif; font-weight: 700; font-size: 32px; color: var(--cream);
    white-space: nowrap;
  }
  .abv {
    position: absolute; left: 0; right: 0; top: 530px; text-align: center;
    font-family: "Arimo", sans-serif; font-size: 17px; color: var(--wine);
  }
  .nutrition {
    position: absolute; left: 22px; top: 430px; width: 130px; padding: 6px 8px;
    background: var(--cream); border: 1.5px solid var(--ink);
    font-family: "Arimo", sans-serif; font-size: 10px; color: var(--ink);
  }
  .nutrition h3 { font-size: 13px; border-bottom: 3px solid var(--ink); padding-bottom: 3px; margin-bottom: 4px; }
  .nutrition p { border-bottom: 1px solid var(--ink); padding: 3px 0; }
  .nutrition p:last-child { border-bottom: none; }
  .base-band {
    position: absolute; left: 0; right: 0; bottom: 0; height: 100px;
    background: var(--wine); border-top: 3px solid var(--gold-deep);
  }
  .tagline {
    position: absolute; left: 0; right: 0; bottom: 12px; text-align: center;
    font-family: "Kaushan Script", cursive; font-size: 64px; color: var(--cream);
    text-shadow: 2px 3px 0 rgba(0,0,0,.35);
  }
</style>
</head>
<body>
<div class="canvas">
  <div class="label">
    <div class="category">Cider</div>
    <h1 class="product-name">JAKOB-RUEDI</h1>
    <div class="glow"></div>
    <div class="apple-photo" role="img" aria-label="Photo of green apples with a halved apple and leaves"></div>
    <div class="nutrition">
      <h3>Nutrition Facts</h3>
      <p>Serving Size 330 ml</p>
      <p>Calories 120</p>
      <p>Sugars 26 g</p>
      <p>Sodium 10 mg</p>
      <p>Vitamin C 2%</p>
    </div>
    <div class="product-type">APPLE CIDER</div>
    <div class="abv">ALC.0.5%. BY VOL.</div>
    <div class="base-band"></div>
    <div class="tagline">Alcohole Free</div>
  </div>
</div>
</body>
</html>
```